Counseling Practice Business Card

I need a professional looking business card incorporating my new logo that was just completed. Card needs to incorporate my name and title, description of my specialty, my address, my phone number, my fax number, my email and my website URL. I need to be able to choose design on/with different paper colors and textures.
I do not have a lot of business card ideas so I am open to anything but I want bold,sharp, clear card without additional designs other than my logo (see attached file info). I am open to different color backgrounds or paper colors including black. I do not like traditional brackets around area codes in phone number or dashes between numbers in phone number. Am open to other ways of presenting including periods between numbers as appropriate. I do not know enough to know what I like yet but I want card to coordinate and work together with my logo. My practice emphasizes natural mental health interventions so any use of color (with background paper color or the blue and green in my logo) that elicits nature is nice. In addition to black, any natural brown or wood looking background might be desirable also. Most of the offerings so far look very similar and boring.

Target Market(s)

Potential therapy clients and other professionals

Contact Information for Business Card

Card information:
Gerald P. Whitcombe, Ph.D.
Licensed Clinical Psychologist
Integrative Health Coach
5214 Ambergate Blvd NW
Suite 815
Fernwood, NC 27599
(770) 555-0143 phone
(770) 555-0178 fax
drgeraldwhitcombe@examplemail.net
brightpathwellness.example

Font styles to use
Serif
Sans Serif
Other font styles liked:
• anything that you think looks crisp, clear and easily readable

Requirements
Must have
• Any color used should coordinate with my logo design (see attached files).
• Card should be printed horizontally so top and bottom are longest sides of rectangle.
• Background color or paper color should complement and highlight logo. Do not like a white background. black, grey, brown or any color my logo would blend well with.
Nice to have
• I would like designer to utilize color to highlight letters/name or phone-fax-web symbols.
• Bottom edge of card could be highlighted if appropriate to an idea.
Should not have
• I would NOT want the card to have a pure white background at all.
• No clear cards.
• Cards should be oriented with long sides on bottom and top, NOT sides. DO NOT LIKE THIS THIN TALL ORIENTATION.

```html
<!DOCTYPE html>
<html lang="en">
<head>
<meta charset="utf-8">
<title>Brightpath Wellness – Business Card</title>
<link rel="stylesheet" href="https://fonts.googleapis.com/css2?family=Open+Sans:wght@400;600&display=swap">
<style>
  :root {
    --page: #ffffff;
    --card: #1d1d1f;
    --blue: #1f75b9;
    --green: #146b3a;
    --ink: #f2f2f2;
    --rule: #8a8a8a;
  }
  html, body {
    margin: 0;
    width: 1200px;
    height: 1200px;
    overflow: hidden;
    background: var(--page);
    font-family: "Open Sans", Arial, sans-serif;
  }
  .card {
    position: absolute;
    left: 282px;
    width: 637px;
    height: 364px;
    background: var(--card);
    overflow: hidden;
  }
  .card--front { top: 182px; }
  .card--back { top: 570px; }

  .brand-name {
    position: absolute;
    margin: 0;
    color: var(--blue);
    font-weight: 600;
    white-space: nowrap;
    letter-spacing: -0.3px;
  }
  .card--front .brand-name {
    left: 30px;
    top: 164px;
    width: 264px;
    font-size: 25px;
    text-align: center;
  }
  .card--back .brand-name {
    left: 0;
    right: 0;
    top: 150px;
    font-size: 44px;
    text-align: center;
  }

  .divider {
    position: absolute;
    left: 303px;
    top: 82px;
    width: 2px;
    height: 198px;
    background: var(--rule);
  }
  .contact {
    position: absolute;
    left: 322px;
    top: 80px;
    color: var(--ink);
    font-size: 16px;
    line-height: 20px;
  }
  .contact__name {
    margin: 0 0 3px;
    color: var(--blue);
    font-size: 22px;
    line-height: 26px;
    font-weight: 600;
  }
  .contact__titles, .contact__lines, .contact__address {
    margin: 0;
    padding: 0;
    list-style: none;
  }
  .contact__lines { margin-top: 6px; }
  .contact__lines li {
    display: flex;
    align-items: center;
    gap: 5px;
    white-space: nowrap;
  }
  .contact__lines svg { width: 13px; height: 13px; flex: none; }
  .contact__email { font-size: 15px; letter-spacing: -0.2px; }
  .contact__address { margin-top: 6px; }

  .edge-band {
    position: absolute;
    left: 0;
    right: 0;
    bottom: 0;
    height: 34px;
    background: var(--green);
    border-top: 8px solid var(--blue);
  }
</style>
</head>
<body>
  <section class="card card--front">
    <p class="brand-name">Brightpath Wellness</p>
    <div class="divider"></div>
    <div class="contact">
      <h1 class="contact__name">Gerald P. Whitcombe, Ph.D.</h1>
      <ul class="contact__titles">
        <li>Licensed Clinical Psychologist</li>
        <li>Integrative Health Coach</li>
      </ul>
      <ul class="contact__lines">
        <li>
          <svg viewBox="0 0 14 14" aria-hidden="true"><circle cx="7" cy="7" r="6.3" fill="none" stroke="var(--blue)" stroke-width="1.2"/><path d="M4.5 3.8c.6-.4 1.1 0 1.3.6l.3.9c.1.4-.2.7-.5.9.4.9 1 1.5 1.9 1.9.2-.3.5-.6.9-.5l.9.3c.6.2 1 .7.6 1.3-.5.8-1.5.9-2.4.4C5.8 9.5 4.4 8.1 3.9 6.4c-.3-1 0-2.1.6-2.6z" fill="var(--blue)"/></svg>
          770.555.0143
        </li>
        <li>
          <svg viewBox="0 0 14 14" aria-hidden="true"><circle cx="7" cy="7" r="6.8" fill="var(--blue)"/><rect x="3.6" y="5.4" width="6.8" height="4.4" rx="0.6" fill="var(--card)"/><rect x="4.8" y="3.6" width="4.4" height="2" fill="var(--card)"/></svg>
          770.555.0178
        </li>
        <li class="contact__email">
          <svg viewBox="0 0 14 14" aria-hidden="true"><circle cx="7" cy="7" r="6.8" fill="var(--blue)"/><rect x="3.4" y="4.4" width="7.2" height="5.2" rx="0.6" fill="var(--card)"/><path d="M3.6 4.8 7 7.4l3.4-2.6" fill="none" stroke="var(--blue)" stroke-width="0.9"/></svg>
          drgeraldwhitcombe@examplemail.net
        </li>
        <li>
          <svg viewBox="0 0 14 14" aria-hidden="true"><circle cx="7" cy="7" r="6.8" fill="var(--blue)"/><circle cx="7" cy="7" r="3.6" fill="none" stroke="var(--card)" stroke-width="1"/><path d="M3.4 7h7.2M7 3.4c-1.5 1.8-1.5 5.4 0 7.2M7 3.4c1.5 1.8 1.5 5.4 0 7.2" fill="none" stroke="var(--card)" stroke-width="0.8"/></svg>
          brightpathwellness.example
        </li>
      </ul>
      <ul class="contact__address">
        <li>5214 Ambergate Blvd NW Suite 815</li>
        <li>Fernwood, NC 27599</li>
      </ul>
    </div>
    <div class="edge-band"></div>
  </section>

  <section class="card card--back">
    <p class="brand-name">Brightpath Wellness</p>
  </section>
</body>
</html>
```